International NeuroCoach and NeuroLeadership expert needs an innovative UNIQUE website

I'm a speaker, trainer, consultant, coach for corporations and organizations, needing a new website with 10 tabs. The final design should incorporate a kaleidoscope theme of color and brain imaging (preferrably images that look like connections or electricity/lightening); must communicate immediate results, evidence/brain-based results, and uniqueness.

Target Market(s)

Corporations and organizations worldwide. Senior leaders: Directors through C-Suite.

Number of Pages Required

5+ page

Font styles to use
Sans Serif

Colors
85acd3
3176b5
3276b5

Requirements
Must have
• Unique design
Nice to have
• See attachment

```html
<!DOCTYPE html>
<html lang="en">
<head>
<meta charset="utf-8">
<title>Marisa Lindqvist – NeuroLeadership</title>
<link href="https://fonts.googleapis.com/css2?family=Raleway:wght@400;500;600;700&display=swap" rel="stylesheet">
<style>
:root{
  --navy:#252c57;
  --navy-soft:#4e5378;
  --blue:#3176b5;
  --blue-light:#85acd3;
  --ink:#222;
  --grey-bg:#ededed;
  --grey-box:#e2e2e2;
  --white:#fff;
}
*{margin:0;padding:0;box-sizing:border-box}
html,body{width:1200px;height:3868px;overflow:hidden;background:var(--white)}
body{font-family:'Raleway',sans-serif;color:var(--ink);position:relative}
.abs{position:absolute}
/* header */
.brand{left:0;width:1200px;top:28px;text-align:center}
.brand-mark{display:inline-block;width:44px;height:44px;border:3px solid var(--navy);border-radius:50%}
.brand-name{font-size:20px;font-weight:600;letter-spacing:1px;color:var(--navy);margin-top:6px}
.top-contact{right:80px;top:70px;font-size:12px;color:#7a8aa8;display:flex;gap:18px;align-items:center}
.top-contact span{display:flex;gap:6px;align-items:center}
.rule{left:80px;width:1040px;top:123px;height:1px;background:var(--blue-light)}
.nav{left:80px;width:1040px;top:140px;display:flex;justify-content:space-between;align-items:center;font-size:13px;color:#4b5b80;text-align:center;line-height:1.1}
/* hero */
.hero-art{left:80px;top:188px;width:1040px;height:560px;background:radial-gradient(circle at 50% 55%,#c7b8ff 0%,#6b5be0 18%,#2a3a9e 45%,#161a4a 75%,#0c0d20 100%)}
.hero-card{left:646px;top:502px;width:426px;height:298px;background:var(--blue);color:var(--white);font-size:31px;line-height:42px;padding:62px 40px 0 42px}
.portrait{left:80px;top:748px;width:506px;height:510px;background:linear-gradient(160deg,#c9c9c9,#6e6e6e 60%,#2d2d2d)}
.quote-panel{left:586px;top:748px;width:534px;height:510px;background:var(--navy);color:var(--white)}
.quote-text{left:646px;top:886px;width:450px;font-size:20px;line-height:28px;color:var(--white)}
.quote-by{left:646px;top:1117px;font-size:14px;line-height:28px;color:var(--white);font-weight:500}
/* activities */
.section-title{left:0;width:1200px;text-align:center;color:var(--navy);font-size:38px;font-weight:600}
.card{top:1420px;width:328px}
.card-img{position:absolute;top:40px;left:0;width:328px;height:315px}
.card-date{position:absolute;top:0;left:0;width:96px;height:92px;background:var(--blue-light);color:var(--white);padding:10px 0 0 25px}
.card-date b{display:block;font-size:38px;font-weight:500;line-height:40px}
.card-date i{font-style:normal;font-size:19px}
.card-meta{position:absolute;top:378px;width:328px;text-align:center;font-size:14px}
.card-title{position:absolute;top:408px;width:328px;text-align:center;font-size:22px;line-height:28px}
.card-link{position:absolute;top:486px;width:328px;text-align:center;font-size:14px;color:var(--blue)}
.card-link span{border-bottom:1px solid var(--blue);padding-bottom:3px}
/* grey band */
.band{left:0;top:1968px;width:1200px;height:1197px;background:var(--grey-bg)}
.video{left:80px;top:2028px;width:327px;height:240px;background:linear-gradient(135deg,#8e9b6a,#4d5a36 60%,#2e3522)}
.play{left:218px;top:2118px;width:56px;height:56px;border-radius:50%;background:rgba(255,255,255,.55)}
.col-head{color:var(--blue);font-size:25px;font-weight:600}
.caps{font-size:15px;font-weight:600;line-height:24px;text-transform:uppercase}
.bullets{list-style:none;font-size:15px;line-height:23.5px}
.bullets li{position:relative;padding-left:17px}
.bullets li::before{content:"";position:absolute;left:2px;top:10px;width:5px;height:5px;background:var(--ink)}
.expertise{list-style:none;font-size:15px;line-height:19px}
.expertise li{padding:6px 0;border-bottom:1px solid #bbb;margin-bottom:12px}
.call-btn{left:513px;top:3053px;width:174px;height:48px;border-radius:12px;background:#000;color:var(--white);font-size:14px;font-weight:700;display:flex;align-items:center;justify-content:center}
.testimonial{left:791px;top:2025px;width:329px;height:315px;background:var(--grey-box);text-align:center}
.avatar{position:absolute;left:98px;top:48px;width:134px;height:134px;border-radius:50%;background:linear-gradient(160deg,#cfd6df,#8795a8)}
.qmark{position:absolute;font-size:52px;font-weight:700;color:var(--navy);line-height:1}
.ocean{left:791px;top:2367px;width:329px;height:194px;background:linear-gradient(180deg,#304a78 0%,#d98b5a 45%,#2b4d77 60%,#1f3f63 100%)}
.imagine{left:791px;top:2561px;width:329px;height:314px;background:var(--blue);color:var(--white);padding:32px 22px 0 22px}
.imagine h4{font-size:14px;font-weight:700;margin-bottom:18px}
.imagine p{font-size:15px;line-height:23.5px}
/* partners */
.partners{left:80px;width:1040px;top:3390px;display:flex;justify-content:space-around;align-items:center}
.partner{font-size:24px;font-weight:600;color:#333;display:flex;align-items:center;gap:8px}
.partner i{display:inline-block;width:18px;height:18px;background:#555}
.dots{left:0;width:1200px;top:3512px;display:flex;justify-content:center;gap:14px}
.dots span{width:8px;height:8px;border-radius:50%;background:var(--blue)}
/* footer */
.footer{left:0;top:3575px;width:1200px;height:293px;background:var(--navy-soft);color:var(--white)}
.f-logo{left:94px;top:3640px;width:240px;text-align:center}
.f-logo .brand-mark{border-color:var(--white);width:56px;height:56px}
.f-logo div.n{font-size:30px;font-weight:600;letter-spacing:1px;margin-top:10px}
.f-copy{left:90px;top:3798px;font-size:13px}
.f-head{font-size:24px;font-weight:600}
.f-line{font-size:13px;line-height:18px;display:flex;gap:10px}
.f-links{font-size:13px;line-height:24px}
.socials{left:507px;top:3788px;display:flex;gap:13px}
.socials span{width:22px;height:22px;border-radius:50%;border:1.5px solid var(--white)}
</style>
</head>
<body>

<header>
  <div class="abs brand"><div class="brand-mark"></div><div class="brand-name">MARISA LINDQVIST</div></div>
  <div class="abs top-contact">
    <span><svg width="12" height="12" viewBox="0 0 24 24"><path d="M6 2l4 4-2 3a12 12 0 0 0 7 7l3-2 4 4-3 4C10 22 2 14 2 5z" fill="#7a8aa8"/></svg>+1.555.010.4422</span>
    <span><svg width="14" height="10" viewBox="0 0 14 10"><rect width="14" height="10" fill="#7a8aa8"/><path d="M0 0l7 6 7-6" stroke="#fff" fill="none"/></svg>drm@lindqvistlead.com</span>
  </div>
  <div class="abs rule"></div>
  <nav class="abs nav">
    <span>Home</span><span>Meet Dr. Marisa</span><span>Speaking</span><span>NeuroCoaching</span>
    <span>NeuroLeadership &amp;<br>Communication Consulting</span><span>Organizational<br>Rejuvination</span>
    <span>News &amp; Media</span><span>Results</span><span>Learn</span><span>Contact</span>
  </nav>
</header>

<section>
  <div class="abs hero-art" role="img" aria-label="Kaleidoscope fractal pattern in violet and blue"></div>
  <div class="abs portrait" role="img" aria-label="Black and white portrait of Dr. Marisa"></div>
  <div class="abs quote-panel"></div>
  <div class="abs hero-card">Dr. Marisa synergizes communication to profoundly transform teams and relationships</div>
  <p class="abs quote-text">“ Dr. Marisa’s business knowledge and broad industry network are invaluable, and she can lead discussions from the front when required, however more often she will guide groups to reach the right answers under their own direction, therefore increasing their confidence and personal awareness. ”</p>
  <p class="abs quote-by">— GRAHAM WHITLOW,<br>CHIEF EXECUTIVE, SCOTLAND HOSPITALITY INDUSTRY</p>
</section>

<section>
  <h2 class="abs section-title" style="top:1330px">Upcoming Activities</h2>
  <div class="abs card" style="left:80px">
    <div class="card-img" role="img" aria-label="City skyline at dusk with harbour statue" style="background:linear-gradient(180deg,#3d5fa8,#1c2c5c 70%,#c69a4a)"></div>
    <div class="card-date"><b>21</b><i>OCT</i></div>
    <p class="card-meta">Lorem Ipsum is simply dummy text</p>
    <p class="card-title">Lorem Ipsum is simply<br>dummy text</p>
    <p class="card-link"><span>Read More</span></p>
  </div>
  <div class="abs card" style="left:436px">
    <div class="card-img" role="img" aria-label="Pagoda at sunset among blossoms" style="background:linear-gradient(180deg,#f0a24a,#c9532e 50%,#e8c8c8)"></div>
    <div class="card-date"><b>19</b><i>FEB</i></div>
    <p class="card-meta">Lorem Ipsum is simply dummy text</p>
    <p class="card-title">Lorem Ipsum is simply<br>dummy text</p>
    <p class="card-link"><span>Read More</span></p>
  </div>
  <div class="abs card" style="left:792px">
    <div class="card-img" role="img" aria-label="Iron tower over a city at golden hour" style="background:linear-gradient(180deg,#7ea4c8,#c7cbd0 45%,#d99a3e 80%,#4d5a2f)"></div>
    <div class="card-date"><b>02</b><i>JUN</i></div>
    <p class="card-meta">Lorem Ipsum is simply dummy text</p>
    <p class="card-title">Lorem Ipsum is simply<br>dummy text</p>
    <p class="card-link"><span>Read More</span></p>
  </div>
</section>

<section>
  <div class="abs band"></div>
  <div class="abs video" role="img" aria-label="Video still of Dr. Marisa outdoors"></div>
  <div class="abs play"></div>
  <svg class="abs" style="left:237px;top:2134px" width="22" height="24"><path d="M0 0l22 12-22 12z" fill="#fff"/></svg>

  <h3 class="abs col-head" style="left:80px;top:2320px">Statistics</h3>
  <p class="abs caps" style="left:80px;top:2375px;width:330px">Companies with strategically engaged employees are more productive and more profitable:</p>
  <ul class="abs bullets" style="left:80px;top:2467px;width:325px">
    <li>Organizations that have over 50% employee engagement retain over 80% of their customers (Metric Insight, 2013)</li>
    <li>Every employee that crosses over from being disengaged to engaged adds an incremental $13,000 to the bottom line each year</li>
    <li>Disengaged employees cost Organizations $3,400 a year for every $10,000 in annual salary (Hale, 2013).</li>
    <li>Organizations with engaged employees outperform those with low employee engagement by 202%. (WorkplaceWeekly, 2016)</li>
    <li>Unengaged employees cost an average of $392 per employee safety incident, compared to just $63 for an engaged employee (Brightbrew Co)</li>
  </ul>

  <h3 class="abs col-head" style="left:436px;top:2028px">Harmonia Consulting</h3>
  <p class="abs caps" style="left:436px;top:2080px;width:290px">Neuroscience-based communication and leadership consulting and coaching results of working with Dr. Marisa:</p>
  <ul class="abs bullets" style="left:436px;top:2230px;width:330px">
    <li>Increased team dynamics, trust, and cooperation</li>
    <li>Fewer stalled or failed projects</li>
    <li>Escape spending so much of time ‘refereeing’ among warring teams and committees</li>
    <li>Altered relationships for increased engagement, productivity, and efficiency</li>
    <li>Less time spent in meetings &amp; less work duplication</li>
    <li>Enhanced internal communication for greater shareholder return</li>
    <li>Diminished need for conflict intervention or mediation</li>
    <li>Strengthened management ability to be effective in responding to resistance to change</li>
  </ul>
  <p class="abs caps" style="left:436px;top:2648px;font-size:14px">Dr. Marisa provides expertise in:</p>
  <ul class="abs expertise" style="left:436px;top:2680px;width:330px">
    <li>Organizational consulting</li>
    <li>Altering communication patterns</li>
    <li>Developing international and diverse teams</li>
    <li>Leadership progression and advancement: front-line to C-Suite</li>
    <li>Executive and communication coaching</li>
    <li>Transforming organizational culture</li>
    <li>Enhancing morale, engagement, and commitment</li>
    <li style="border:none">Implementing successful change initiatives</li>
  </ul>
  <div class="abs call-btn">Call Now</div>

  <div class="abs testimonial">
    <span class="qmark" style="left:40px;top:38px">“</span>
    <div class="avatar" role="img" aria-label="Portrait of a smiling client"></div>
    <span class="qmark" style="left:257px;top:160px">”</span>
    <p style="position:absolute;top:210px;left:30px;width:270px;font-size:13px;line-height:20px">“Lorem Ipsum is simply dummy text of the printing and typesetting industry.</p>
    <p style="position:absolute;top:262px;width:329px;font-size:13px">Lorem Ipsum</p>
  </div>
  <div class="abs ocean" role="img" aria-label="Sunset over the ocean with waves"></div>
  <div class="abs imagine">
    <h4>TAKE A MOMENT TO IMAGINE...</h4>
    <p>Imagine if your team had better internal communication? What would be the results? Embraced change initiatives, improved employee engagement, shorter meetings, followed direction and delegation, things done right the first time. What results could you see from improved internal communication and what results would you like to see?</p>
  </div>
</section>

<section>
  <h2 class="abs section-title" style="top:3220px;line-height:48px">Working with<br>Top Executives &amp; Organization</h2>
  <div class="abs partners">
    <span class="partner">Harbourline</span>
    <span class="partner" style="font-size:18px">Crestbay Resort</span>
    <span class="partner"><i></i>Northgate Hotels</span>
    <span class="partner" style="font-size:20px;color:#777">Solara Tourism</span>
  </div>
  <div class="abs dots"><span></span><span></span><span></span></div>
</section>

<footer>
  <div class="abs footer"></div>
  <div class="abs f-logo"><div class="brand-mark"></div><div class="n">MARISA LINDQVIST</div></div>
  <p class="abs f-copy">© 2020. MarisaLindqvist. All rights reserved.</p>
  <h4 class="abs f-head" style="left:505px;top:3626px">Contact</h4>
  <div class="abs" style="left:510px;top:3665px;color:#fff">
    <p class="f-line" style="margin-bottom:10px"><svg width="14" height="10" viewBox="0 0 14 10"><rect width="14" height="10" fill="#fff"/><path d="M0 0l7 6 7-6" stroke="#4e5378" fill="none"/></svg>DrM@lindqvistlead.com</p>
    <p class="f-line" style="margin-bottom:10px"><svg width="13" height="13" viewBox="0 0 24 24"><path d="M6 2l4 4-2 3a12 12 0 0 0 7 7l3-2 4 4-3 4C10 22 2 14 2 5z" fill="#fff"/></svg>+1.555.010.4422</p>
    <p class="f-line"><svg width="12" height="16" viewBox="0 0 12 16"><path d="M6 0a6 6 0 0 1 6 6c0 4-6 10-6 10S0 10 0 6a6 6 0 0 1 6-6z" fill="#fff"/><circle cx="6" cy="6" r="2" fill="#4e5378"/></svg><span>Greater Lakeside Area, 1200 Alder Road<br>Fernwood | WA | 98000 | USA</span></p>
  </div>
  <div class="abs socials"><span></span><span></span><span></span><span></span><span></span></div>
  <h4 class="abs f-head" style="left:930px;top:3626px">Links</h4>
  <div class="abs f-links" style="left:930px;top:3666px">
    <p>Meet Dr. Marisa</p><p>Expertise in..</p><p>Speaking</p><p>Results</p><p>Content Library</p><p>Contact</p>
  </div>
</footer>

</body>
</html>
```